Simply recommend a cartwella theme that will best suit our business

FIRSTLY, To avoid a shotgun approach to submissions and to ensure contestants actually put THOUGHT to their submission and its qualification of our requirements below, EACH CONTESTANT MAY ONLY SUBMIT 3 SELECTIONS. IF YOU SUBMIT MORE YOUR ENTIRE SET WILL BE DELETED AND YOU WILL BE REMOVED FROM THE CONTEST.

[login to view URL] will be our new home. You can see [login to view URL] we are preparing our consumer market purchasing wellness and nutritional supplements online for our new business model.
We would like our new e-com site to cater to showcasing our supplements with a strong sorting function i.e. by brand, ailment, tag etc. Responsive, interactive, mobile-centric, e-com focused with an ability to catalogue many products. Customers must be able to create a profile that remembers their orders and delivery address and give them the opportunity to select repeat order and date of requested delivery and frequency etc.

We would like to run a contest to see which freelancer recommends the Cartwella theme that best suits our needs accordingly. You may always look at what other companies with a similar function are using.

These are some of the requirements we have of the theme: (as many of them as possible)

TRIAL OPTION TO QUALIFY THEME
MUST BE MOBILE CENTRIC
ACCESS TO VIDMARO AND SOCIAL MEDIA
PRODUCT GROUPING BY AILMENT, BRAND,
SUBSCRIBE TO NEWSLETTER
SLIDERS, HEADER SLIDE SHOW
LOG IN
REGISTER
AI READY, LIVE CHAT READY
DOWNLOADABLE PDF - DETAILED PRODUCT INFO
SIZE CHOICES ON A PRODUCT LINE
SORT BY CATEGORY / KEYWORD / ASSORTED PACK / BRAND
SHARE TO SOCIAL MEDIA
COUPON CODE
DRIVE CONVERSIONS WHEREVER THE CUSTOMER IS
FAST CHECK OUT / CART AND ADD TO CART
PROMOTE SPECIALS, DISCOUNTS, GROUPING, FEATURED, NEW PRODUCT DISPLAYS
HOME PAGE VIDEO
MULTI COLUM DROP DOWN MENU - MOBILE CENTRIC
FULL-WIDTH LAYOUT
FREE STOCK PHOTOS
SUPPORT / UPGRADES
SEARCH ENGINE OPTIMISED
FAST LOADING SPEED
MAGAZINE TYPE PIXLORENA / PALSTREAM FEED INTEGRATION OR BLOG TO SOCIAL MEDIA
INTEGRATION CAPABILITY TO OTHER APPS SUCH AS STOCKHAVEN, INVOXTRON, QUBA ETC

PLEASE ENSURE TO SUBMIT THE LINK AND THE SCREENSHOT OF THE HOMEPAGE FOR EACH SUBMISSION.

A FREELANCER THAT SUBMITS A THEME FIRST HAS RIGHT TO THAT SUBMISSION IF DUPLICATES ARE SUBMITTED BY ANOTHER FREELANCER.

Also, preview the submissions of the other contestants as mentioned to ensure you don't waste a submission on an already submitted theme.

```html
<!DOCTYPE html>
<html lang="en">
<head>
<meta charset="utf-8">
<title>vessa — Storefront Home</title>
<link rel="stylesheet" href="https://fonts.googleapis.com/css2?family=Poppins:wght@400;500;600;700&display=swap">
<style>
  :root {
    --promo-red: #ef6a5a;
    --white: #ffffff;
    --ink: #1e1e1e;
    --hero-stone: #b8ada4;
    --hero-stone-dark: #a99d93;
    --panel-sand: #d8bea8;
    --panel-sand-dark: #b88d6e;
    --panel-grey: #c6c4c0;
    --panel-khaki: #a8916d;
    --cookie-bg: rgba(32, 32, 32, 0.94);
    --muted: #a9a9a9;
  }
  * { box-sizing: border-box; margin: 0; padding: 0; }
  html, body { width: 1200px; height: 1179px; overflow: hidden; }
  body { font-family: "Poppins", sans-serif; background: var(--white); color: var(--ink); position: relative; }

  .promo-bar {
    position: absolute; left: 0; top: 0; width: 1200px; height: 59px;
    background: var(--promo-red); color: var(--white);
    display: flex; align-items: center; justify-content: center;
    font-weight: 600; font-size: 19px; letter-spacing: 0.2px;
  }

  .site-header {
    position: absolute; left: 0; top: 59px; width: 1200px; height: 80px;
    background: var(--white);
  }
  .site-header svg { position: absolute; }
  .icon-menu { left: 22px; top: 22px; }
  .icon-search { left: 118px; top: 23px; }
  .icon-account { left: 1028px; top: 19px; }
  .icon-cart { left: 1116px; top: 22px; }
  .brand-name {
    position: absolute; left: 0; right: 0; top: 10px; text-align: center;
    font-weight: 600; font-size: 46px; letter-spacing: -1px; color: var(--ink);
  }
  .cart-count {
    position: absolute; left: 1139px; top: 11px; width: 36px; height: 36px;
    border-radius: 50%; background: var(--ink); color: var(--white);
    font-size: 17px; font-weight: 600; display: flex; align-items: center; justify-content: center;
  }

  .hero {
    position: absolute; left: 0; top: 139px; width: 1200px; height: 618px;
    background: linear-gradient(90deg, var(--hero-stone) 0%, var(--hero-stone) 55%, var(--hero-stone-dark) 80%, var(--hero-stone) 100%);
  }
  .hero-copy {
    position: absolute; left: 60px; top: 175px; width: 650px; text-align: center; color: var(--white);
  }
  .hero-title { font-weight: 700; font-size: 38px; letter-spacing: 1.5px; line-height: 1; }
  .hero-rule { width: 64px; height: 3px; background: var(--white); margin: 28px auto 0; }
  .hero-text { font-size: 18.5px; line-height: 38px; margin-top: 26px; }
  .btn {
    display: flex; align-items: center; justify-content: center;
    background: var(--white); color: var(--ink);
    font-weight: 600; font-size: 19px; letter-spacing: 1.5px;
  }
  .hero-btn { width: 300px; height: 63px; margin: 36px auto 0; }
  .hero-scroll { position: absolute; left: 580px; top: 568px; }

  .feature-new {
    position: absolute; left: 0; top: 757px; width: 604px; height: 422px;
    background: radial-gradient(ellipse at 55% 30%, var(--panel-sand-dark) 0%, var(--panel-sand) 55%);
  }
  .feature-restock {
    position: absolute; left: 604px; top: 757px; width: 596px; height: 422px;
    background: radial-gradient(ellipse at 50% 70%, var(--panel-khaki) 0%, var(--panel-grey) 55%);
  }
  .restock-badge {
    position: absolute; left: 193px; top: 149px; width: 214px; height: 214px;
    border: 3px solid var(--white); border-radius: 50%;
    display: flex; flex-direction: column; align-items: center; justify-content: center;
    color: var(--white); font-weight: 600; font-size: 27px; letter-spacing: 1.5px; line-height: 32px;
  }
  .restock-badge .underline { border-bottom: 2px solid var(--white); line-height: 30px; }
  .panel-btn { position: absolute; width: 270px; height: 70px; padding-bottom: 10px; align-items: flex-end; }
  .feature-new .panel-btn { left: 168px; top: 386px; }
  .feature-restock .panel-btn { left: 165px; top: 386px; }

  .cookie-notice {
    position: absolute; left: 32px; top: 960px; width: 583px; height: 195px;
    background: var(--cookie-bg); color: var(--white); padding: 20px 22px 0;
  }
  .cookie-text { font-size: 18.5px; line-height: 37px; }
  .cookie-actions { position: absolute; right: 22px; top: 151px; display: flex; gap: 20px; align-items: center; font-size: 18.5px; }
  .cookie-policy { color: var(--muted); }
  .cookie-accept { font-weight: 600; letter-spacing: 1px; display: flex; align-items: center; gap: 10px; }
</style>
</head>
<body>
  <div class="promo-bar">MID-SEASON SALE UP TO 70% OFF. SHOP NOW</div>

  <header class="site-header">
    <svg class="icon-menu" width="40" height="32" viewBox="0 0 40 32" aria-label="Menu"><g stroke="#1e1e1e" stroke-width="3"><line x1="0" y1="4" x2="38" y2="4"/><line x1="0" y1="15" x2="38" y2="15"/><line x1="0" y1="26" x2="38" y2="26"/></g></svg>
    <svg class="icon-search" width="34" height="34" viewBox="0 0 34 34" aria-label="Search"><circle cx="13" cy="13" r="11" fill="none" stroke="#1e1e1e" stroke-width="3"/><line x1="21" y1="21" x2="32" y2="32" stroke="#1e1e1e" stroke-width="3"/></svg>
    <div class="brand-name">vessa</div>
    <svg class="icon-account" width="38" height="40" viewBox="0 0 38 40" aria-label="Account"><circle cx="19" cy="12" r="10" fill="none" stroke="#1e1e1e" stroke-width="2.5"/><path d="M3 38c0-9 7-14 16-14s16 5 16 14z" fill="none" stroke="#1e1e1e" stroke-width="2.5"/></svg>
    <svg class="icon-cart" width="36" height="38" viewBox="0 0 36 38" aria-label="Cart"><path d="M1 4h6l5 20h18l4-14H10" fill="none" stroke="#1e1e1e" stroke-width="2.5" stroke-linejoin="round"/><circle cx="14" cy="32" r="3" fill="none" stroke="#1e1e1e" stroke-width="2.5"/><circle cx="27" cy="32" r="3" fill="none" stroke="#1e1e1e" stroke-width="2.5"/></svg>
    <div class="cart-count">0</div>
  </header>

  <section class="hero" role="img" aria-label="Woman seated in a patterned navy jumpsuit holding a red handbag against a warm grey wall">
    <div class="hero-copy">
      <h1 class="hero-title">COSMOPOLIS</h1>
      <div class="hero-rule"></div>
      <p class="hero-text">Quisquemos sodales suscipit tortor ditaemcos condimentum de<br>cosmo lacus meleifend menean diverra loremous.</p>
      <div class="btn hero-btn">SHOP NOW</div>
    </div>
    <svg class="hero-scroll" width="46" height="24" viewBox="0 0 46 24" aria-label="Scroll down"><polyline points="2,2 23,21 44,2" fill="none" stroke="#ffffff" stroke-width="2"/></svg>
  </section>

  <section class="feature-new" role="img" aria-label="Woman in a brown knit top with a pink sleeve, looking down">
    <div class="btn panel-btn">SHOP NOW</div>
  </section>

  <section class="feature-restock" role="img" aria-label="Woman with a bob haircut in a khaki utility shirt dress">
    <div class="restock-badge"><span>BACK</span><span>TO</span><span class="underline">STOCK</span></div>
    <div class="btn panel-btn">SHOP NOW</div>
  </section>

  <aside class="cookie-notice">
    <p class="cookie-text">The cookie settings on this website are set to 'allow all cookies' to give you the very best experience. Please click Accept Cookies to continue to use the site.</p>
    <div class="cookie-actions">
      <span class="cookie-policy">PRIVACY POLICY</span>
      <span class="cookie-accept">ACCEPT <svg width="18" height="16" viewBox="0 0 18 16" aria-hidden="true"><polyline points="2,9 7,14 16,2" fill="none" stroke="#ffffff" stroke-width="2.5"/></svg></span>
    </div>
  </aside>
</body>
</html>
```